Business Card Design for Kind Helper

I am starting my own consultancy business, using what I learned in marketing and advertising to help Non -profits with marketing and communications needs. I need a professional business card design to hand out to my clients.

My business name is “Outreach2Kindness” my vision is that this need this to be reflective of marketing doing good for the world through the power of communications. I like the color palettes in olives, creams and oranges but am open to design options.
In addition to the cards I am asking for separate file for the logo and will need a JPG, PSD Vector File.

Information to go on the card:

Morwenna Calloway
Marketing Consultant
Email: outreach2kindness@mailbrook.com, callowaym1@brinmoreu.edu
Website: Outreach2Kindness.com

Communications

```html
<!DOCTYPE html>
<html lang="en">
<head>
<meta charset="utf-8">
<title>Outreach2Kindness — Business Card</title>
<link rel="stylesheet" href="https://fonts.googleapis.com/css2?family=Urbanist:wght@400;600;700&display=swap">
<style>
  :root {
    --card-bg: #ffffff;
    --ink: #000000;
    --text-grey: #3b3b3b;
    --brand-red: #c4000c;
  }
  html, body {
    margin: 0;
    padding: 0;
    overflow: hidden;
    background: var(--card-bg);
  }
  .business-card {
    position: relative;
    width: 1200px;
    height: 686px;
    background: var(--card-bg);
    font-family: "Urbanist", sans-serif;
    color: var(--text-grey);
    overflow: hidden;
  }
  .brand-mark {
    position: absolute;
    left: 44px;
    top: 14px;
    width: 246px;
    height: 246px;
    background: var(--brand-red);
  }
  .brand-name {
    position: absolute;
    left: 308px;
    top: 66px;
    margin: 0;
    font-size: 70px;
    font-weight: 600;
    line-height: 1;
    color: var(--ink);
    letter-spacing: -0.5px;
  }
  .person-name {
    position: absolute;
    left: 22px;
    top: 388px;
    margin: 0;
    font-size: 47px;
    font-weight: 700;
    line-height: 1;
  }
  .person-title {
    position: absolute;
    left: 18px;
    top: 450px;
    margin: 0;
    font-size: 34px;
    font-weight: 400;
    line-height: 1;
  }
  .contact-list {
    position: absolute;
    left: 580px;
    top: 506px;
    margin: 0;
    padding: 0;
    list-style: none;
    font-size: 36px;
    font-weight: 400;
    line-height: 52px;
  }
  .website {
    position: absolute;
    left: 364px;
    top: 628px;
    margin: 0;
    font-size: 38px;
    font-weight: 400;
    line-height: 1;
  }
</style>
</head>
<body>
  <main class="business-card">
    <div class="brand-mark" aria-hidden="true"></div>
    <h1 class="brand-name">Outreach2Kindness.com</h1>

    <p class="person-name">Morwenna Calloway</p>
    <p class="person-title">Marketing Consultant</p>

    <ul class="contact-list">
      <li class="contact-email">outreach2kindness@mailbrook.com</li>
      <li class="contact-email">callowaym1@brinmoreu.edu</li>
    </ul>

    <p class="website">Outreach2Kindness.com</p>
  </main>
</body>
</html>
```